Trvmlegal.com needs a wedsite. Law Office of Darnell P. Whitby

Darnell P. Whitby is a criminal law firm that is 5 years old. We have already had all the content written and now just need the website designed. We also just finished our logo design using Pixel Harbor and would like it used in the design of the website.

Industry/Entity Type

Law Firm

Number of Pages Required

5+ page

Requirements
Must have
• I was our new logo to be on the website also. I want Dallas sites as the stock pictures for the website. For example the Grey Stone Tribunal. I also need to be able to add YouTube videos. It has to adjust to be seen on computers and also cell phones. I need to be able to have a information sheet for clients to fill out and submit back to me.

```html
<!DOCTYPE html>
<html lang="en">
<head>
<meta charset="utf-8">
<title>Law Office of Darnell P. Whitby</title>
<link href="https://fonts.googleapis.com/css2?family=Oswald:wght@400;500&family=Open+Sans:wght@400;600;700&display=swap" rel="stylesheet">
<style>
:root{
  --blue:#1e5aa8;
  --blue-bright:#2d8fe0;
  --navy:#0e2a57;
  --hero-dark:#1f2d46;
  --ink:#222;
  --muted:#555;
  --page:#e9e9ea;
  --panel:#ffffff;
  --side:#d9d9db;
  --footer:#2e2e2f;
  --footer-line:#4a4a4c;
  --star:#f07d19;
}
*{margin:0;padding:0;box-sizing:border-box}
html,body{width:812px;height:1200px;overflow:hidden}
body{position:relative;background:var(--page);font-family:"Open Sans",Arial,sans-serif;color:var(--ink)}
.abs{position:absolute}

/* header */
.header{left:0;top:0;width:812px;height:106px;background:linear-gradient(#fff,#dedfe1)}
.header-rule{left:0;top:0;width:812px;height:4px;background:var(--navy)}
.brand{left:126px;top:8px;width:108px;height:94px;display:flex;flex-direction:column;align-items:center;justify-content:center;gap:6px}
.brand-dot{width:38px;height:38px;border-radius:50%;background:var(--navy)}
.brand-name{font-size:9px;font-weight:700;color:var(--navy);text-align:center;line-height:11px}
.call{left:392px;top:11px;font-family:"Oswald",sans-serif;font-weight:500;font-size:17px;color:var(--blue);letter-spacing:.3px}
.phones{left:392px;top:36px;width:298px;display:flex;justify-content:space-between}
.phone{text-align:center;border-top:1px solid #bbb;padding-top:2px;width:88px}
.phone small{display:block;font-size:8px;color:#444}
.phone b{font-family:"Oswald",sans-serif;font-weight:500;font-size:14px;color:var(--navy)}
.nav{left:278px;top:78px;width:408px;height:28px;background:var(--blue);display:flex;align-items:center;justify-content:space-around;padding:0 4px}
.nav span{font-size:8.5px;color:#fff;font-weight:600;padding:0 6px;border-right:1px solid rgba(255,255,255,.35)}
.nav span:last-child{border:none}

/* hero */
.hero{left:0;top:106px;width:812px;height:284px;background:linear-gradient(180deg,#35435e,var(--hero-dark) 70%,#2a3956)}
.hero-person{left:190px;top:114px;width:176px;height:200px;background:linear-gradient(#6b6f78,#2a2d35)}
.hero-text{left:400px;top:124px;width:280px;text-align:center;color:#fff}
.hero-text .l1{font-family:"Oswald",sans-serif;font-size:25px;letter-spacing:1px;line-height:30px}
.hero-text .l2{font-family:"Oswald",sans-serif;font-size:42px;color:var(--blue-bright);line-height:42px}
.hero-text .l3{font-family:"Oswald",sans-serif;font-size:16px;line-height:22px}
.hero-btn{left:408px;top:223px;width:262px;height:31px;background:var(--blue);color:#fff;font-family:"Oswald",sans-serif;font-size:16px;display:flex;align-items:center;justify-content:center}
.badges{left:410px;top:262px;width:262px;height:36px;display:flex;align-items:center;gap:8px}
.badge{width:34px;height:34px;border-radius:50%;background:#c9ccd2;border:2px solid #8d929b}
.badge.wide{width:80px;height:22px;border-radius:2px;background:#b79a4c;border:none}
.badge.tag{width:28px;height:30px;border-radius:3px;background:#d0d4dc;border:none}

.grey-band{left:0;top:390px;width:812px;height:48px;background:#bdbdbf}
.card{width:260px;height:112px;top:316px;background:#fff;padding:4px;box-shadow:0 1px 3px rgba(0,0,0,.3)}
.card-img{width:100%;height:100%;background:linear-gradient(#eeeeef,#aeb3bb)}
.card-cap{left:4px;right:4px;bottom:4px;height:48px;background:rgba(30,30,32,.85);padding:6px 10px}
.card-cap h3{font-family:"Oswald",sans-serif;font-weight:400;font-size:12px;color:var(--blue-bright);letter-spacing:.3px}
.card-cap p{font-size:7px;color:#fff;line-height:9.5px;margin-top:3px}

/* main */
.main{left:116px;top:440px;width:570px;height:486px;background:var(--panel)}
.content{left:126px;top:458px;width:348px;height:460px;overflow:hidden}
.content h1{font-weight:400;font-size:14px;color:#111;padding-bottom:5px;border-bottom:1px solid #ddd}
.content h1 em{font-style:normal;color:var(--blue)}
.lead{font-size:10.5px;line-height:13.5px;color:#222;margin:8px 0 5px}
.content p{font-size:6.8px;line-height:11.2px;color:var(--muted)}
.content .sub{color:var(--blue);font-size:7.5px;margin-top:4px}
.feature{display:flex;gap:10px;margin-top:14px}
.feature-img{flex:none;width:140px;height:96px;background:linear-gradient(#f4f4f4,#d8d2cc);border:1px solid #ddd}

.side{left:486px;top:458px;width:192px;height:462px}
.side-box{width:100%;background:var(--side);border-radius:4px;padding:6px}
.side-title{font-family:"Oswald",sans-serif;font-size:11px;color:#fff;display:inline-block;background:#111;padding:0 3px;margin-bottom:6px}
.side-title em{font-style:normal;background:var(--blue);padding:0 3px}
.video{width:100%;height:90px;background:#111;position:relative}
.video-bar{position:absolute;left:8px;right:8px;bottom:8px;height:7px;display:flex;align-items:center;gap:6px}
.video-bar i{display:block;flex:1;height:2px;background:#666}
.field{height:16px;background:#fff;border:1px solid #c8c8c8;font-size:6.5px;color:#444;padding:3px 5px;margin-bottom:3px}
.field.tall{height:30px}
.check{font-size:6px;color:#888;margin:3px 0}
.captcha{display:flex;justify-content:space-between;align-items:flex-end}
.captcha span{background:#fff;border:1px solid #bbb;font-family:Georgia,serif;font-style:italic;font-size:10px;padding:1px 5px}
.send{background:var(--blue);color:#fff;font-size:8px;font-weight:700;padding:3px 12px}
.profile{height:110px;background:var(--blue);display:flex;padding:5px;gap:6px;position:relative}
.profile-photo{width:74px;height:100px;background:linear-gradient(#b8c3cf,#5e6b7b);position:relative}
.profile-photo span{position:absolute;left:0;right:0;bottom:0;background:#eee;font-size:6.5px;font-weight:700;color:var(--navy);text-align:center;padding:2px 0}
.profile p{font-size:6.3px;line-height:10px;color:#fff;width:82px}

/* testimonials */
.testi{left:0;top:926px;width:812px;height:108px;background:#fff}
.testi-photo{left:130px;top:940px;width:94px;height:94px;border-radius:50%;background:linear-gradient(#9aa6b4,#40495a);border:4px solid var(--navy)}
.testi-body{left:234px;top:940px;width:432px}
.testi-body h2{font-family:"Oswald",sans-serif;font-weight:400;font-size:13px;color:#222;letter-spacing:.4px;border-bottom:1px solid #ddd;padding-bottom:2px}
.testi-body h2 em{font-style:normal;color:var(--navy);font-weight:500}
.who{font-size:7.5px;font-weight:700;color:var(--navy);margin-top:4px}
.role{font-size:6.5px;color:var(--blue)}
.testi-body p{font-size:6.8px;line-height:11.5px;color:var(--muted);margin-top:5px}
.stars{left:608px;top:958px;color:var(--star);font-size:11px;letter-spacing:1px}
.more{left:584px;top:1016px;width:82px;height:14px;background:var(--navy);color:#fff;font-size:6.5px;font-weight:600;display:flex;align-items:center;justify-content:center}
.arrows{left:670px;top:1018px;display:flex;gap:2px}
.arrows i{width:9px;height:9px;background:#777;display:block}

/* footer */
.footer{left:0;top:1034px;width:812px;height:166px;background:var(--footer);border-top:3px solid var(--blue)}
.fcol{top:1050px}
.fcol h4{font-family:"Oswald",sans-serif;font-weight:500;font-size:11px;color:#fff;letter-spacing:.4px;display:flex;align-items:center;gap:5px;border-bottom:1px solid var(--footer-line);padding-bottom:3px}
.fcol ul{list-style:none}
.fcol li{font-size:7px;color:#ddd;height:16.4px;line-height:16px;border-bottom:1px solid var(--footer-line);padding-left:8px;position:relative}
.fcol li::before{content:"›";position:absolute;left:0;color:#aaa}
.loc{font-size:7px;color:#ddd;line-height:10px;display:flex;gap:6px;margin-top:8px}
.loc b{color:var(--blue-bright);font-weight:400}
.foot-rule{left:124px;top:1166px;width:564px;height:1px;background:var(--blue)}
.copy{left:124px;top:1172px;font-size:6.3px;color:#bbb;line-height:10px}
.copy b{color:var(--blue-bright);font-weight:600}
.social{left:598px;top:1174px;display:flex;gap:4px}
.social i{width:13px;height:13px;border-radius:50%;background:#5a5a5c;display:block}
</style>
</head>
<body>

<div class="abs header"></div>
<div class="abs header-rule"></div>
<div class="abs brand">
  <div class="brand-dot"></div>
  <div class="brand-name">Law Office of<br>Darnell P. Whitby</div>
</div>
<div class="abs call">CALL TODAY FOR A FREE CASE REVIEW</div>
<div class="abs phones">
  <div class="phone"><small>D. WHITBY</small><b>972.555.0148</b></div>
  <div class="phone"><small>D. WHITBY</small><b>972.555.0148</b></div>
  <div class="phone"><small>D. WHITBY</small><b>972.555.0148</b></div>
</div>
<nav class="abs nav">
  <span>HOME</span><span>WORK'S COMP &#8964;</span><span>SOCIAL SECURITY</span><span>ATTORNEYS</span><span>BLOG</span><span>CONTACT US</span>
</nav>

<section class="abs hero" role="img" aria-label="Dallas downtown skyline seen from above in blue tones"></section>
<div class="abs hero-person" role="img" aria-label="Portrait of the attorney in a suit with arms crossed"></div>
<div class="abs hero-text">
  <div class="l1">PAY NO FEES UNTIL</div>
  <div class="l2">YOU RECEIVE</div>
  <div class="l3">COMPENSATION FOR YOUR CLAIM!</div>
</div>
<div class="abs hero-btn">Don't Give Up Your Rights! Call Today!</div>
<div class="abs badges">
  <i class="badge"></i><i class="badge"></i><i class="badge"></i><i class="badge"></i><i class="badge wide"></i><i class="badge tag"></i>
</div>

<div class="abs grey-band"></div>
<div class="abs card" style="left:130px">
  <div class="card-img" role="img" aria-label="Social security disability claim form on a desk"></div>
  <div class="abs card-cap"><h3>SOCIAL SECURITY CLAIMS</h3><p>If your claim was denied, don't go down without a fight. We'll put our experience to work for you.</p></div>
</div>
<div class="abs card" style="left:420px">
  <div class="card-img" role="img" aria-label="Team of colleagues meeting around a laptop"></div>
  <div class="abs card-cap"><h3>WORKERS' COMP CLAIMS</h3><p>We'll work tirelessly to ensure you receive the best settlement for your workers' compensation claim.</p></div>
</div>

<div class="abs main"></div>
<article class="abs content">
  <h1>Our Aggressive Criminal Defense Team <em>Fights for You</em></h1>
  <p class="lead">You are innocent unless proven guilty. But our criminal justice system often unjustly denies this fundamental constitutional right. The Law Office of Darnell P. Whitby seeks to balance the scales of justice.</p>
  <p>Our Dallas-Fort Worth law firm solely handles criminal defense cases so we can dedicate our full resources to the pursuit of justice. Our criminal defense attorneys presume that every case we take will go to trial and aggressively advocate for you from the moment we take your case. Because the wheels of justice spin 24 hours, so do we. If you are arrested after-hours, on weekends or on holidays, we are available to handle your jail release.</p>
  <p class="sub">Darnell P. Whitby</p>
  <p>Darnell P. Whitby is the managing partner of our law firm. Before founding his own practice, he worked for one of the best criminal defense law firms in the Dallas-Fort Worth area, where he advocated for clients accused of drug, murder, assault and other serious offenses.</p>
  <p>Darnell's lifelong career goal was to become a criminal defense trial attorney. His studies at Northvale University School of Law reflect his single-minded intention of honing his courtroom skills and knowledge about criminal law. Darnell won several regional advocacy contests and was runner up in multiple national competitions. His professors and peers voted for Darnell as one of the ten best advocates in the</p>
  <div class="feature">
    <div class="feature-img" role="img" aria-label="Judge's gavel resting beside law books"></div>
    <div>
      <p class="sub" style="margin-top:0">Renata Sloane-Price</p>
      <p>Renata Sloane-Price acts as Of-Counsel for the Law Office of Darnell P. Whitby. As a founding partner of VANCE | PRICE, Renata delivers experienced representation to our clients. Prior to founding VANCE | PRICE, Renata worked for a prominent law firm in Dallas, Texas, where she tried cases in the state and federal courts.</p>
    </div>
  </div>
  <p class="sub">Our Dallas Attorneys Protect Your Rights to Justice</p>
  <p>You have the right to remain silent and to have an attorney present for questioning. You should exercise these constitutional rights when charged with a serious crime. Do not say anything since even a seemingly innocent statement could lead to incriminating evidence and trying to talk your way out of it could have the opposite effect. Ask for a lawyer then call the Law Office of Darnell P. Whitby for help.</p>
  <p>The Law Office of Darnell P. Whitby exclusively represents clients in criminal defense matters. Our team is available 24-7 to take your case immediately following your arrest in Dallas, Tarrant</p>
</article>

<aside class="abs side">
  <div class="side-box">
    <div class="side-title">MEET <em>MARCUS ELLORY</em></div>
    <div class="video" role="img" aria-label="Embedded introduction video">
      <div class="video-bar">
        <svg width="7" height="7" viewBox="0 0 7 7"><path d="M1 0L7 3.5L1 7Z" fill="#ccc"/></svg><i></i>
      </div>
    </div>
  </div>
  <div class="side-box" style="margin-top:8px">
    <div class="side-title">CONTACT <em>US</em></div>
    <div class="field">Name:</div>
    <div class="field">Email:</div>
    <div class="field">Phone:</div>
    <div class="field tall">Message:</div>
    <div class="check">&#9634; I have read the disclaimer</div>
    <div class="captcha"><span>TcDW</span><div class="send">SEND</div></div>
  </div>
  <div class="side-box" style="margin-top:8px">
    <div class="side-title">ATTORNEY <em>PROFILE</em></div>
    <div class="profile">
      <div class="profile-photo" role="img" aria-label="Attorney portrait"><span>Darnell P. Whitby</span></div>
      <p>Darnell P. Whitby is the managing partner of our law firm. Before founding his own practice, he worked for one of the best criminal defense law firms in the area.</p>
      <svg class="abs" style="left:118px;bottom:8px" width="24" height="8" viewBox="0 0 24 8"><path d="M5 1L2 4L5 7M19 1L22 4L19 7" stroke="#fff" stroke-width="1.5" fill="none"/></svg>
    </div>
  </div>
</aside>

<section class="abs testi"></section>
<div class="abs testi-photo" role="img" aria-label="Client portrait"></div>
<div class="abs testi-body">
  <h2>CLIENT <em>TESTIMONIALS</em></h2>
  <div class="who">Paul Hendry</div>
  <div class="role">Business Owner</div>
  <p>My daughter's father has a drug problem. He never completed his treatment program and I suspected that he was using drugs during his supervised visits with our daughter. Ms. Carrow helped me to get his supervised visitations suspended. It is a relief to know that my daughter will be safe and not exposed to drug abuse by her father</p>
</div>
<div class="abs stars">&#9733;&#9733;&#9733;&#9733;&#9733;</div>
<div class="abs more">MORE TESTIMONIALS</div>
<div class="abs arrows"><i></i><i></i></div>

<footer class="abs footer"></footer>
<div class="abs fcol" style="left:124px;width:108px">
  <h4><svg width="10" height="9"><rect x="0.5" y="0.5" width="9" height="8" fill="none" stroke="#fff"/><path d="M2 3H8M2 5H8" stroke="#fff"/></svg>NAVIGATION</h4>
  <ul><li>HOME</li><li>PRACTICE AREAS</li><li>MEET MARCUS</li><li>REVIEWS</li><li>BLOG</li></ul>
</div>
<div class="abs fcol" style="left:246px;width:232px">
  <h4><svg width="11" height="9"><rect x="0.5" y="2.5" width="10" height="6" fill="#fff"/><rect x="3.5" y="0.5" width="4" height="2" fill="none" stroke="#fff"/></svg>PRACTICE AREAS</h4>
  <div style="display:flex;gap:16px">
    <ul style="width:108px"><li>MURDER</li><li>MURDER</li><li>SEXUAL OFFENSES</li><li>EXPUNGEMENTS</li><li>NON-DISCLOSURES</li></ul>
    <ul style="width:108px"><li>EARLY PROBATION</li><li>RELEASE</li><li>PROBATION VIOLATIONS</li><li>DWI, DUI</li><li>DRUG OFFENSES</li></ul>
  </div>
</div>
<div class="abs fcol" style="left:492px;width:196px">
  <h4 style="border:none"><svg width="8" height="10"><path d="M4 10C4 10 0 5.5 0 4A4 4 0 0 1 8 4C8 5.5 4 10 4 10Z" fill="#fff"/><circle cx="4" cy="4" r="1.5" fill="#2e2e2f"/></svg>LOCATIONS</h4>
  <div style="display:flex;gap:12px">
    <div class="loc"><svg width="7" height="9"><path d="M3.5 9C3.5 9 0 5 0 3.5A3.5 3.5 0 0 1 7 3.5C7 5 3.5 9 3.5 9Z" fill="#2d8fe0"/></svg><span><b>Adress :</b> 48 Elm Crest<br>Road Dallas, Texas<br>Contrary to popular</span></div>
    <div>
      <div class="loc"><svg width="8" height="8"><path d="M1 1L3 0.5L4 3L3 4Q4 5.5 5 5L6 4L8 5L7.5 7.5Q3 8 0.5 2Z" fill="#2d8fe0"/></svg>214 (555) - 0193</div>
      <div class="loc"><svg width="9" height="7"><rect width="9" height="7" fill="#2d8fe0"/><path d="M0 0L4.5 4L9 0" stroke="#2e2e2f" fill="none"/></svg>info@trvmlegal.com</div>
    </div>
  </div>
</div>
<div class="abs foot-rule"></div>
<div class="abs copy">Copyright &copy; 2015 by Law Offices Of Darnell P. Whitby All Rights Reserved.<br>Attorney Marketing by <b>Darnell P. Whitby</b></div>
<div class="abs social"><i></i><i></i><i></i><i></i><i></i><i></i></div>

</body>
</html>
```